Biz card for my counselling/social work practice

Biz card design for my counselling practice, focus on well-being, I am a social worker who also teaches meditation and workshops but my main focus for the card is my counselling practice. My website reveals a gentle flowing quality which I would life reflected in my card. This business card will be designed to share with other practitioners who are looking for support with their clients to take their healing to another level or well-being.

Target Market(s)

professionals seeking mental health counselling/men/women/ those seeking to improve their well-being through insight based counselling to optimize their lives and process trauma or limiting patterns

Industry/Entity Type

Counsellor

Contact Information for Business Card

Info on the card: perhaps text is aligned left?
Marla Finch, MSW, RSW
Counsellor
250.555.0142
info@marlafinch.ca
www.marlafinch.ca

Please use a modern font doesn’t need to be the one chosen below. Thank you

Font styles to use
Serif

Colors
3176b5
33a6d7
33b8a4
6b449b
abd037
d2a4cc
e55fa2

Requirements
Must have
• My business card details on front
• Backside
• Accelerated Resolution Therapy
• Cognitive Behavioral Therapy
• Mindfulness Informed Therapy
Nice to have
• I would like the card to be basic, (white or creme without too much bold colour) and with perhaps a stripe or band of vertical colour in blue or green (or a merge of colour) perhaps embossed or in a negative space. (this is one idea, but do not want the card to be too feminine or interest only women as i see men too so this is only an idea, but not 100 percent on this.
• I do not have a logo. I would prefer to heart from my website not to be used in the design as i am considering modifying this and re-branding.
Should not have
• too bold colours or bright yellow/blacks. i Like tones that are greens, blues.

```html
<!DOCTYPE html>
<html lang="en">
<head>
<meta charset="utf-8">
<title>Marla Finch — Business Card</title>
<link rel="stylesheet" href="https://fonts.googleapis.com/css2?family=Roboto:wght@500&family=Work+Sans:wght@400;500;600&display=swap">
<style>
  :root {
    --backdrop: #1b1b1b;
    --paper: #efefef;
    --ink: #2b2b2b;
    --brand-purple: #5e3897;
    --back-purple: #6b449b;
    --accent-green: #abd037;
    --white: #ffffff;
    --emboss: #e9e9e9;
  }
  * { margin: 0; padding: 0; box-sizing: border-box; }
  html, body { width: 1200px; height: 897px; overflow: hidden; }
  body { background: var(--backdrop); position: relative; font-family: "Work Sans", sans-serif; }

  .card { position: absolute; left: 326px; width: 549px; height: 299px; }
  .card-front { top: 126px; background: var(--paper); }
  .card-back { top: 473px; background: var(--back-purple); color: var(--white); }

  .identity { position: absolute; right: 254px; top: 127px; text-align: right; white-space: nowrap; }
  .identity-name { font-family: "Roboto", sans-serif; font-weight: 500; font-size: 21px; color: var(--brand-purple); line-height: 1; }
  .identity-role { font-size: 13.5px; color: var(--ink); letter-spacing: 0.4px; margin-top: 2px; line-height: 1.1; }

  .divider { position: absolute; left: 316px; top: 128px; width: 1px; height: 43px; background: var(--brand-purple); }

  .contact { position: absolute; left: 340px; top: 122px; list-style: none; }
  .contact-item { display: flex; align-items: center; gap: 4px; font-size: 13.5px; color: var(--ink); letter-spacing: 0.5px; height: 18px; white-space: nowrap; }
  .contact-icon { width: 8px; height: 8px; flex: none; }

  .emboss-mark { position: absolute; left: 446px; top: 216px; width: 74px; height: 60px; border-radius: 30px 30px 36px 36px; background: var(--emboss); box-shadow: 0 1px 2px rgba(0,0,0,0.12); }

  .welcome { position: absolute; left: 114px; top: 70px; white-space: nowrap; }
  .welcome-title { font-weight: 500; font-size: 30px; letter-spacing: 1.8px; line-height: 1; }
  .welcome-sub { font-size: 17px; letter-spacing: 0.9px; margin-top: 8px; line-height: 1; }

  .services { position: absolute; left: 114px; top: 154px; list-style: none; }
  .service { display: flex; align-items: center; gap: 9px; font-size: 17px; letter-spacing: 1.2px; height: 27.5px; white-space: nowrap; }
  .service::before { content: ""; width: 12px; height: 12px; background: var(--accent-green); flex: none; }
</style>
</head>
<body>
  <section class="card card-front" aria-label="Card front">
    <div class="identity">
      <p class="identity-name">Marla Finch, MSW, RSW</p>
      <p class="identity-role">Counsellor</p>
    </div>
    <div class="divider"></div>
    <ul class="contact">
      <li class="contact-item">
        <svg class="contact-icon" viewBox="0 0 10 10" aria-hidden="true"><path d="M2 1 L4 1 L4.6 3 L3.4 3.8 Q4.4 6 6.2 6.6 L7 5.4 L9 6 L9 8 Q8 9.2 6.5 8.8 Q2.5 7.5 1.2 3.5 Q0.8 2 2 1Z" fill="var(--brand-purple)"/></svg>
        250.555.0142
      </li>
      <li class="contact-item">
        <svg class="contact-icon" viewBox="0 0 10 10" aria-hidden="true"><rect x="0.8" y="2" width="8.4" height="6" fill="none" stroke="var(--brand-purple)" stroke-width="1"/><path d="M0.8 2 L5 5.5 L9.2 2" fill="none" stroke="var(--brand-purple)" stroke-width="1"/></svg>
        info@marlafinch.ca
      </li>
      <li class="contact-item">
        <svg class="contact-icon" viewBox="0 0 10 10" aria-hidden="true"><g fill="none" stroke="var(--brand-purple)" stroke-width="0.8"><circle cx="5" cy="5" r="4.2"/><ellipse cx="5" cy="5" rx="1.8" ry="4.2"/><path d="M0.8 5 H9.2 M1.5 2.8 H8.5 M1.5 7.2 H8.5"/></g></svg>
        www.marlafinch.ca
      </li>
    </ul>
    <div class="emboss-mark" role="img" aria-label="Blind-embossed mark"></div>
  </section>

  <section class="card card-back" aria-label="Card back">
    <div class="welcome">
      <h1 class="welcome-title">A GENTLE START</h1>
      <p class="welcome-sub">Talk, Coaching, Movement &amp; Care</p>
    </div>
    <ul class="services">
      <li class="service">Accelerated Resolution Therapy</li>
      <li class="service">Cognitive Behavioral Therapy</li>
      <li class="service">Mindfulness Informed Therapy</li>
    </ul>
  </section>
</body>
</html>
```